2018 Harborline Constable's Legal Companion

Cover, spine and back cover for Police Officer Law book. The overall size of the cover is 18.82 x 11 (with the .25 inch bleed it is 19.32 x 11.5) and the spine is 1.82 x 11 plus (1.82 x 11.5 with the bleed). The book also has a companion cruiser good for motor vehicle law which is smaller about 5X7 inches with a spiral binding. The Motor Vehicle guide should have a similar design but with a motor vehicle theme to it. The year (2018) should be prominent because it changes every year. I attached the last two book designs. I'd like them to be distinctively different each year.

Target Market(s)

Massachusetts Police Officers

Requirements
Must have
• Companion motor vehicle guide with similar design yet a motor vehicle theme or twist to it. Professional text book type look.
Nice to have
• real life image or images
Should not have
• Images of police who are obviously not US police.

```html
<!DOCTYPE html>
<html lang="en">
<head>
<meta charset="utf-8">
<title>2018 Harborline Constable's Legal Companion – Cover Set</title>
<link rel="stylesheet" href="https://fonts.googleapis.com/css2?family=Tinos:wght@400;700&family=Montserrat:wght@800&family=Jost:wght@600&family=Open+Sans:wght@400;700&family=Arimo:wght@700&display=swap">
<style>
  :root{
    --navy-deep:#0a1140;
    --navy:#16277a;
    --navy-glow:#2a44b0;
    --gold:#fcc52a;
    --white:#ffffff;
    --frame:#c9c9c9;
    --page:#ffffff;
    --ink:#111111;
  }
  *{margin:0;padding:0;box-sizing:border-box}
  html,body{width:1200px;height:1140px;overflow:hidden;background:var(--page)}
  .sheet{position:relative;width:1200px;height:1140px}
  .sheet-frame{position:absolute;left:1px;top:1px;width:1198px;height:1138px;border:1.5px solid var(--frame);border-radius:16px}

  .cover{position:absolute;overflow:hidden;
    background:radial-gradient(ellipse at 50% 45%,var(--navy-glow) 0%,var(--navy) 45%,var(--navy-deep) 100%)}
  .cover-main{left:96px;top:84px;width:1015px;height:565px}
  .cover-guide{left:374px;top:744px;width:545px;height:303px}

  .wave{position:absolute;left:0;bottom:0;width:100%;height:100%}
  .spine{position:absolute;top:0;height:100%;border-left:1px solid rgba(0,0,0,.45);border-right:1px solid rgba(0,0,0,.45)}
  .cover-main .spine{left:462px;width:90px}
  .cover-guide .spine{left:249px;width:48px}

  .brand{position:absolute;display:flex;align-items:center;gap:5px;color:var(--gold);
    font-family:"Jost",sans-serif;font-weight:600;letter-spacing:.08em}
  .brand-dot{border-radius:50%;background:var(--gold)}

  /* back cover */
  .back-copy{position:absolute;left:63px;top:61px;width:336px;color:var(--white);
    font-family:"Open Sans",sans-serif;font-size:6.4px;line-height:8.7px;text-align:justify}
  .back-copy p{margin-bottom:8px}
  .emblem{float:left;width:132px;height:122px;margin:30px 14px 4px 0;border-radius:10px;
    background:radial-gradient(circle at 50% 50%,#ffd44f 0%,#e0a91a 60%,rgba(224,169,26,0) 72%)}
  .rights{position:absolute;font-family:"Arimo",sans-serif;font-weight:700;color:var(--navy-deep)}
  .cover-main .rights{left:67px;top:532px;font-size:12px}
  .cover-guide .rights{left:36px;top:283px;font-size:6.5px}

  /* spine type */
  .spine-type{position:absolute;display:flex;align-items:center;transform:rotate(-90deg)}
  .spine-year{font-family:"Montserrat",sans-serif;font-weight:800;color:var(--white);line-height:1}
  .spine-title{display:flex;flex-direction:column;font-family:"Tinos",serif;color:var(--gold);line-height:1}
  .spine-title .small{font-weight:700}
  .cover-main .spine-type{left:-170px;top:210px;width:430px;height:90px;gap:14px}
  .cover-main .spine-year{font-size:58px}
  .cover-main .spine-title .small{font-size:17px}
  .cover-main .spine-title .large{font-size:32px;margin-top:3px}
  .cover-guide .spine-type{left:-100px;top:110px;width:248px;height:48px;gap:7px}
  .cover-guide .spine-year{font-size:31px}
  .cover-guide .spine-title .small{font-size:9px}
  .cover-guide .spine-title .large{font-size:16.5px;margin-top:2px}

  /* front cover */
  .front{position:absolute;top:0;height:100%;text-align:center}
  .cover-main .front{left:552px;width:463px}
  .cover-guide .front{left:297px;width:248px}
  .kicker{position:absolute;left:0;width:100%;font-family:"Tinos",serif;font-weight:700;color:var(--gold)}
  .headline{position:absolute;left:0;width:100%;font-family:"Tinos",serif;color:var(--gold);line-height:1}
  .year{position:absolute;left:0;width:100%;font-family:"Montserrat",sans-serif;font-weight:800;color:var(--white);line-height:1}
  .author{position:absolute;left:0;width:100%;font-family:"Jost",sans-serif;font-weight:600;color:var(--gold)}
  .author-role{position:absolute;left:0;width:100%;font-family:"Tinos",serif;color:var(--white)}

  .cover-main .kicker{top:168px;font-size:19px}
  .cover-main .headline{top:192px;font-size:40px}
  .cover-main .year{top:240px;font-size:132px;letter-spacing:-2px}
  .guide-label{position:absolute;left:0;width:100%;top:379px;font-family:"Jost",sans-serif;font-weight:600;font-size:16px;color:var(--gold)}
  .guide-list{position:absolute;left:77px;top:399px;width:310px;height:52px;
    border-top:1.5px solid var(--white);border-bottom:1.5px solid var(--white);
    display:grid;grid-template-columns:1.6fr 1fr;padding:5px 4px 0;list-style:none;text-align:left;
    font-family:"Tinos",serif;font-size:15.5px;line-height:19px;color:var(--gold)}
  .guide-list li::before{content:"· "}
  .cover-main .author{top:476px;font-size:15.5px}
  .cover-main .author-role{top:495px;font-size:12px}

  .scene{position:absolute;left:0;top:0;width:100%;height:190px;
    background:linear-gradient(180deg,rgba(180,20,30,.85) 0%,rgba(120,40,110,.55) 35%,rgba(22,39,122,0) 100%),
               radial-gradient(ellipse at 40% 25%,rgba(255,255,255,.6),rgba(255,255,255,0) 45%)}
  .vehicle{position:absolute;left:110px;top:246px;width:125px;height:48px;border-radius:40% 45% 20% 20%;
    background:linear-gradient(160deg,#ff4a3a,#b5121b 60%,#5a0a0e)}
  .cover-guide .kicker{top:120px;font-size:10.5px}
  .cover-guide .year{top:128px;font-size:60px;letter-spacing:-1px}
  .cover-guide .headline{top:196px;font-size:14px}
  .cover-guide .author{top:229px;font-size:8px}
  .cover-guide .author-role{top:239px;font-size:5px}
</style>
</head>
<body>
<main class="sheet">
  <div class="sheet-frame"></div>

  <!-- Full wrap: back, spine, front -->
  <section class="cover cover-main">
    <svg class="wave" viewBox="0 0 1015 565" preserveAspectRatio="none" aria-hidden="true">
      <path d="M0 522 C200 505 390 548 600 545 S880 505 1015 516 L1015 565 L0 565 Z" fill="var(--gold)"/>
    </svg>

    <div class="back-copy">
      <div class="emblem" role="img" aria-label="Gold scales of justice emblem"></div>
      <p>Dana Whitcombe is founder and director of the Northgate Learning Trust, an organization built to support officers and communities through steady training, clear guidance and practical study. Our goal is to help each reader grow in knowledge, confidence and judgment, so they may serve as a pillar to the community they protect.</p>
      <p>Dana spent many years in the field before turning to teaching. She found that new officers often lacked one simple reference that tied statute, procedure and daily practice together in plain words.</p>
      <p>This companion answers that need. Each chapter sets out the law as it stands this year, explains how courts have read it, and shows how it applies on patrol, at the station and in the courtroom. Checklists and short summaries make quick review possible before a shift or an exam.</p>
      <p>Dana now leads workshops across the region, mentoring recruits and veteran officers alike. She lives on the coast with her family and their two dogs.</p>
    </div>
    <div class="rights">2018 Kestrel Training LLC. All Rights Reserved</div>

    <div class="spine">
      <div class="spine-type">
        <span class="spine-year">2018</span>
        <span class="spine-title"><span class="small">Harborline Constable's</span><span class="large">LEGAL COMPANION</span></span>
      </div>
      <div class="brand" style="left:18px;top:536px;font-size:9px"><span class="brand-dot" style="width:8px;height:8px"></span>KESTREL</div>
    </div>

    <div class="front">
      <div class="brand" style="left:175px;top:80px;font-size:20px"><span class="brand-dot" style="width:16px;height:16px"></span>KESTREL</div>
      <div class="kicker">Harborline Constable's</div>
      <div class="headline">LEGAL COMPANION</div>
      <div class="year">2018</div>
      <div class="guide-label">Guide to:</div>
      <ul class="guide-list">
        <li>Criminal procedures</li><li>Motor Vehicle</li>
        <li>Statutory Law</li><li>Juvenile Law</li>
      </ul>
      <div class="author">Lieutenant Marcus D. Redfield, Esq.</div>
      <div class="author-role">The Law Officer</div>
    </div>
  </section>

  <!-- Motor vehicle companion -->
  <section class="cover cover-guide">
    <svg class="wave" viewBox="0 0 545 303" preserveAspectRatio="none" aria-hidden="true">
      <path d="M0 280 C110 272 200 294 330 292 S480 272 545 276 L545 303 L0 303 Z" fill="var(--gold)"/>
    </svg>
    <div class="rights">2018 Kestrel Training LLC. All Rights Reserved</div>

    <div class="spine">
      <div class="spine-type">
        <span class="spine-year">2018</span>
        <span class="spine-title"><span class="small">Harborline Constable's</span><span class="large">LEGAL COMPANION</span></span>
      </div>
      <div class="brand" style="left:5px;top:285px;font-size:6px;gap:3px"><span class="brand-dot" style="width:5px;height:5px"></span>KESTREL</div>
    </div>

    <div class="front">
      <div class="scene" role="img" aria-label="Police cruiser with red and blue light bar at night"></div>
      <div class="brand" style="left:88px;top:68px;font-size:11px;gap:4px"><span class="brand-dot" style="width:9px;height:9px"></span>KESTREL</div>
      <div class="kicker">Harborline Constable's</div>
      <div class="year">2018</div>
      <div class="headline">Motor Vehicle Guide</div>
      <div class="author">Lieutenant Marcus D. Redfield, Esq.</div>
      <div class="author-role">The Law Officer</div>
      <div class="vehicle" role="img" aria-label="Red sports car with a crumpled front after a collision"></div>
    </div>
  </section>
</main>
</body>
</html>
```